Frostwyn.co - Polar Expeditions Specialists

We need a modern, visually striking business card for Frostwyn.co, a company specialized in selling expedition cruises to the most remote regions on Earth, with a focus on the Arctic and Antarctica. The design should instantly communicate that the cardholder is an expert in polar travel. Use clean, premium aesthetics with cool tones like icy blue and white, possibly incorporating polar imagery (ice, glaciers, penguins, etc.)

Attached the logo

Contact Information for Business Card

Feels high-end and trustworthy.. Visually memorable — encourages people to keep it

Colors
0054AA
0677BA
7BADD7
CADEEF
E8F1F8

Requirements
Must have
• ice, glaciers, penguins, montains
Nice to have
• modern, transparente,

```html
<!DOCTYPE html>
<html lang="en">
<head>
<meta charset="utf-8">
<title>Frostwyn.co Business Card</title>
<link href="https://fonts.googleapis.com/css2?family=Poppins:wght@400;600;700&family=Arimo:wght@400&display=swap" rel="stylesheet">
<style>
  :root {
    --bg: #2b2b2e;
    --brand-blue: #2f74bd;
    --deep-blue: #1f4fa3;
    --ice-cyan: #5fe0f7;
    --ink: #222428;
    --muted: #6a6d72;
    --white: #ffffff;
    --divider: #b9bcc2;
    --edge-grey: #6e6f73;
  }
  * { box-sizing: border-box; margin: 0; padding: 0; }
  html, body { width: 1200px; height: 874px; overflow: hidden; background: var(--bg); }
  .stage { position: relative; width: 1200px; height: 874px; }
  .card {
    position: absolute; left: 250px; width: 700px; height: 400px;
    border-radius: 22px; overflow: hidden;
  }
  .card-back { top: 25px; }
  .pattern-fill {
    width: 100%; height: 100%;
    background: linear-gradient(100deg, var(--deep-blue) 0%, var(--brand-blue) 45%, #3aa6dc 75%, var(--ice-cyan) 100%);
  }
  .card-front { top: 449px; background: var(--white); }
  .brand {
    position: absolute; left: 48px; top: 150px; width: 285px;
  }
  .brand-row { display: flex; align-items: center; gap: 10px; white-space: nowrap; }
  .brand-dot { width: 28px; height: 28px; border-radius: 50%; background: var(--brand-blue); flex: none; }
  .brand-name {
    font-family: "Poppins", sans-serif; font-weight: 700; font-size: 34px;
    color: var(--brand-blue); line-height: 1;
  }
  .brand-tagline {
    margin-top: 6px; margin-left: 38px;
    font-family: "Poppins", sans-serif; font-weight: 600; font-size: 11px;
    color: var(--brand-blue); white-space: nowrap;
  }
  .divider {
    position: absolute; left: 350px; top: 40px; width: 1px; height: 230px;
    background: var(--divider);
  }
  .contact { position: absolute; left: 385px; top: 48px; }
  .person-name {
    font-family: "Poppins", sans-serif; font-weight: 600; font-size: 30px;
    color: var(--brand-blue); line-height: 1.1;
  }
  .person-title {
    font-family: "Arimo", sans-serif; font-size: 17px; color: var(--muted);
    margin-bottom: 22px;
  }
  .contact p { font-family: "Arimo", sans-serif; font-size: 18px; color: var(--ink); line-height: 1.3; }
  .contact-lines { margin-top: 12px; }
  .contact-line { display: flex; align-items: center; gap: 10px; }
  .contact-line svg { width: 16px; height: 16px; flex: none; }
  .footer-band {
    position: absolute; left: 0; bottom: 0; width: 700px; height: 62px;
  }
  .website {
    position: absolute; right: 40px; bottom: 18px;
    font-family: "Arimo", sans-serif; font-size: 19px; color: var(--white);
  }
</style>
</head>
<body>
<div class="stage">
  <section class="card card-back">
    <div class="pattern-fill" role="img" aria-label="Repeating pattern of polar bear marks shading from deep blue to icy cyan"></div>
  </section>

  <section class="card card-front">
    <div class="brand">
      <div class="brand-row">
        <span class="brand-dot"></span>
        <span class="brand-name">Frostwyn.co</span>
      </div>
      <div class="brand-tagline">Polar Expeditions Specialists</div>
    </div>

    <div class="divider"></div>

    <div class="contact">
      <h1 class="person-name">Elias Brandt</h1>
      <div class="person-title">President</div>
      <p>4152 Glacier Row</p>
      <p>Whitehorse, Canada 20418</p>
      <div class="contact-lines">
        <p class="contact-line">
          <svg viewBox="0 0 16 16"><path d="M3 1l3 3-1.5 2a9 9 0 005 5L11.5 9.5l3 3-2 2C6 14 2 10 1.5 3z" fill="var(--brand-blue)"/></svg>
          555-214-8830
        </p>
        <p class="contact-line">
          <svg viewBox="0 0 16 16"><rect x="4" y="1" width="8" height="14" rx="1.5" fill="none" stroke="var(--brand-blue)" stroke-width="1.6"/><circle cx="8" cy="12.5" r="0.9" fill="var(--brand-blue)"/></svg>
          555-309-4127
        </p>
        <p class="contact-line">
          <svg viewBox="0 0 16 16"><rect x="1" y="3" width="14" height="10" fill="var(--brand-blue)"/><path d="M1 3l7 6 7-6" fill="none" stroke="var(--white)" stroke-width="1.3"/></svg>
          info@frostwyn.com
        </p>
      </div>
    </div>

    <svg class="footer-band" viewBox="0 0 700 62" aria-hidden="true">
      <polygon points="0,40 380,40 400,0 700,0 700,62 0,62" fill="var(--edge-grey)"/>
      <polygon points="380,40 420,0 700,0 700,62 340,62" fill="var(--brand-blue)"/>
    </svg>
    <div class="website">www.frostwyn.com</div>
  </section>
</div>
</body>
</html>
```